Automotive component supplier needs a business card design

We need a business card design for our company called Velmar Global Components Ltd based in the UK. We are a supplier of interior and exterior components to premium car manufacturers such as Corvane Hale, Durrant Fyfe, Maxtorn and Valdessimo. We would like to see a modern business card design that uses the colour blue.

Target Market(s)

Premium automotive car manufacturers.

Industry/Entity Type

Automotive

Contact Information for Business Card

Company Name : Velmar Global Components Limited
Address: 17 Tamsey Yard, Upper Drisk, Warwick, CV31 8RJ, United Kingdom
Web Address : www.velmarparts-example.co.uk

Font styles to use
Other font styles liked:
• Helvetica

Colors
3176b5
0255a3
85acd3
cfdeed
cee9f5
85cae6
34a6d7
0692cd
9bcb3c

Requirements
Must have
• Clear company logo and a mixture of blue colours.
Nice to have
• A high quality modern image.
Should not have
• Multiple colours.

```html
<!DOCTYPE html>
<html lang="en">
<head>
<meta charset="utf-8">
<title>Velmar Global Components – Business Card</title>
<link rel="stylesheet" href="https://fonts.googleapis.com/css2?family=Source+Sans+3:wght@400;600;700&display=swap">
<style>
  :root {
    --bg-top: #2a2a2a;
    --bg-bottom: #050505;
    --brand-blue: #0692cd;
    --paper: #ffffff;
    --ink: #3a3a3a;
  }
  html, body {
    margin: 0;
    padding: 0;
    width: 1200px;
    height: 900px;
    overflow: hidden;
  }
  body {
    background: linear-gradient(180deg, var(--bg-top) 0%, #151515 55%, var(--bg-bottom) 100%);
    font-family: "Source Sans 3", Arial, sans-serif;
    position: relative;
  }
  .card {
    position: absolute;
    top: 170px;
    width: 347px;
    height: 561px;
    overflow: hidden;
    box-shadow: 0 6px 18px rgba(0,0,0,0.5);
  }
  .card--front { left: 259px; background: var(--paper); }
  .card--back { left: 631px; background: var(--brand-blue); }

  .accent-bar {
    position: absolute;
    left: 102px;
    width: 143px;
    background: var(--brand-blue);
  }
  .accent-bar--top { top: 0; height: 30px; }
  .accent-bar--bottom { bottom: 0; height: 28px; }

  .brand {
    position: absolute;
    left: 0;
    right: 0;
    text-align: center;
    font-weight: 700;
    line-height: 1;
  }
  .brand__name {
    display: block;
    font-size: 52px;
    letter-spacing: 6px;
    margin-right: -6px;
  }
  .brand__tagline {
    display: block;
    font-size: 14px;
    letter-spacing: 2.4px;
    margin-top: 8px;
  }
  .card--front .brand { top: 148px; color: var(--brand-blue); }
  .card--back .brand { top: 246px; color: var(--paper); }

  .contact {
    position: absolute;
    top: 316px;
    left: 0;
    right: 0;
    text-align: center;
    color: var(--ink);
  }
  .contact__name {
    margin: 0;
    font-size: 21px;
    font-weight: 600;
    color: var(--brand-blue);
    line-height: 1.2;
  }
  .contact__role {
    margin: 1px 0 12px;
    font-size: 15px;
    line-height: 18px;
  }
  .contact__lines {
    list-style: none;
    margin: 0 0 13px;
    padding: 0;
    font-size: 15px;
    line-height: 21px;
  }
  .contact__label {
    color: var(--brand-blue);
    font-weight: 700;
  }
  .contact__address {
    margin: 0;
    font-size: 15px;
    line-height: 17px;
    font-style: normal;
  }
</style>
</head>
<body>
  <section class="card card--front" aria-label="Business card front">
    <div class="accent-bar accent-bar--top"></div>
    <div class="brand">
      <span class="brand__name">VELMAR</span>
      <span class="brand__tagline">GLOBAL COMPONENTS</span>
    </div>
    <div class="contact">
      <h1 class="contact__name">LORNE AVERY</h1>
      <p class="contact__role">Managing Director</p>
      <ul class="contact__lines">
        <li><span class="contact__label">P:</span> 555-014-2260</li>
        <li><span class="contact__label">M:</span> 555-014-2261</li>
        <li><span class="contact__label">E:</span> info@velmarparts-example.co.uk</li>
        <li><span class="contact__label">W:</span> www.velmarparts-example.co.uk</li>
      </ul>
      <address class="contact__address">17 Tamsey Yard, Upper Drisk<br>Warwick, CV31 8RJ</address>
    </div>
    <div class="accent-bar accent-bar--bottom"></div>
  </section>

  <section class="card card--back" aria-label="Business card back">
    <div class="brand">
      <span class="brand__name">VELMAR</span>
      <span class="brand__tagline">GLOBAL COMPONENTS</span>
    </div>
  </section>
</body>
</html>
```